Business card design to suit our website

Need a nice looking business card for our business based off images from our Website and provided images. The business card will require 2 different names (for the 2 owners). The business card should include images from our website, facebook (keel bracket works set) or the pictures provided. it should also contain all contact information.
Our website is www.keelbracketworks.com.au
Please dont use image from top bar of website. If images are used please use the ones of our product under the buy it now tab

Target Market(s)

Automotive

Industry/Entity Type

Automotive Part

Contact Information for Business Card

Business Name. contact details including names phone number email. logo
2 business cards needed with 2 different persons names and phone number.

Colors

Designer to choose colors to be used in the design.

Requirements
Must have
• whatever looks best

```html
<!DOCTYPE html>
<html lang="en">
<head>
<meta charset="utf-8">
<title>Steadfast Bracket Kit – Business Cards</title>
<link rel="stylesheet" href="https://fonts.googleapis.com/css2?family=Roboto:wght@400;700;900&family=Kaushan+Script&display=swap">
<style>
  :root {
    --bg: #2b2b2e;
    --card: #ffffff;
    --red: #c8202f;
    --red-dark: #8f141f;
    --ink: #111111;
    --grey-light: #e6e6e6;
    --gold: #c9a23a;
  }
  * { box-sizing: border-box; margin: 0; padding: 0; }
  html, body { width: 1200px; height: 800px; overflow: hidden; background: var(--bg); }
  body { font-family: "Roboto", Arial, sans-serif; position: relative; }

  .card {
    position: absolute; left: 310px; width: 580px; height: 330px;
    background: var(--card); overflow: hidden;
    box-shadow: 0 10px 30px rgba(0,0,0,.45);
  }
  .card--front { top: 45px; }
  .card--back { top: 425px; }

  .tagline {
    position: absolute; z-index: 2;
    font-family: "Kaushan Script", cursive; font-size: 25px; color: var(--ink); line-height: 1;
  }
  .brand {
    position: absolute; z-index: 2; display: flex; align-items: center; gap: 9px; white-space: nowrap;
  }
  .brand__mark { width: 14px; height: 14px; border-radius: 50%; background: var(--red); flex: none; }
  .brand__name {
    font-weight: 900; font-size: 30px; color: var(--red); letter-spacing: -0.4px; line-height: 1;
  }
  .tread-band { position: absolute; z-index: 1; height: 14px; background: var(--grey-light); }

  .red-band {
    position: absolute; left: 0; right: 0; bottom: 0; height: 46px; z-index: 3;
    background: var(--red);
    border-top: 2px solid var(--red-dark);
    clip-path: polygon(38% 0, 100% 0, 100% 100%, 0 100%, 0 70%, 36% 70%);
  }
  .red-band__text {
    position: absolute; right: 22px; bottom: 12px; z-index: 4; color: #fff;
    font-weight: 700; font-size: 16px; letter-spacing: .3px; white-space: nowrap;
  }

  /* front */
  .flag-area {
    position: absolute; left: 0; top: 60px; width: 240px; height: 150px;
    background: linear-gradient(120deg, #f4f4f4 0%, #bdbdbd 35%, #e9e9e9 55%, #8d8d8d 100%);
  }
  .car-art {
    position: absolute; left: 0; top: 120px; width: 300px; height: 210px;
    background:
      radial-gradient(ellipse at 60% 40%, rgba(255,255,255,.85), rgba(255,255,255,0) 55%),
      linear-gradient(165deg, #eceef0 0%, #b4b8bd 45%, #6f7378 85%, #55585c 100%);
    clip-path: polygon(0 30%, 35% 10%, 70% 2%, 100% 22%, 100% 100%, 0 100%);
  }
  .card--front .tagline { left: 255px; top: 22px; }
  .card--front .brand { left: 225px; top: 62px; }
  .card--front .tread-band { left: 225px; right: 0; top: 100px; }
  .warranty-seal {
    position: absolute; left: 305px; top: 170px; width: 58px; height: 58px;
    border-radius: 50%; background: radial-gradient(circle, #222 48%, var(--gold) 50%, #e8cf7a 75%, var(--gold) 100%);
  }
  .fitment { position: absolute; left: 392px; top: 140px; line-height: 1.3; }
  .fitment__label { font-size: 14px; color: #333; }
  .fitment__model { font-size: 15px; font-weight: 900; color: var(--ink); }
  .fitment__years { font-size: 14px; color: #333; }

  /* back */
  .product-photo {
    position: absolute; right: 0; top: 0; width: 300px; height: 290px;
    background:
      radial-gradient(ellipse at 70% 45%, rgba(196,150,60,.55), rgba(196,150,60,0) 40%),
      radial-gradient(ellipse at 45% 30%, rgba(225,225,220,.9), rgba(225,225,220,0) 45%),
      linear-gradient(150deg, #b9b6ae 0%, #8a867e 40%, #3f3d3a 75%, #9b978f 100%);
    clip-path: polygon(22% 0, 100% 0, 100% 100%, 12% 100%, 6% 82%, 14% 70%, 4% 58%, 12% 44%, 8% 30%, 18% 16%);
  }
  .card--back .tagline { left: 40px; top: 38px; }
  .card--back .brand { left: 40px; top: 80px; }
  .card--back .tread-band { left: 30px; width: 280px; top: 116px; }
  .contact { position: absolute; left: 40px; top: 160px; }
  .contact__name { font-size: 23px; font-weight: 900; color: var(--ink); line-height: 1; }
  .contact__role { font-size: 14px; font-weight: 700; color: var(--red); margin-top: 3px; }
  .contact__list { list-style: none; margin-top: 14px; }
  .contact__item { display: flex; align-items: center; gap: 8px; font-size: 14px; font-weight: 700; color: var(--ink); margin-bottom: 6px; white-space: nowrap; }
  .contact__icon { width: 18px; height: 18px; flex: none; }
</style>
</head>
<body>

<section class="card card--front" aria-label="Card front">
  <div class="flag-area" role="img" aria-label="Chequered racing flag graphic"></div>
  <div class="car-art" role="img" aria-label="Silver illustration of a sedan front"></div>
  <p class="tagline">Made In Australia</p>
  <div class="tread-band"></div>
  <div class="brand"><span class="brand__mark"></span><span class="brand__name">Steadfast Bracket Kit</span></div>
  <div class="warranty-seal" role="img" aria-label="Lifetime warranty seal"></div>
  <div class="fitment">
    <p class="fitment__label">Suits</p>
    <p class="fitment__model">KR-KT CRUISER</p>
    <p class="fitment__model">MX-MY TRAILMAN</p>
    <p class="fitment__years">(2002-Mid 2008)</p>
  </div>
  <div class="red-band"></div>
  <p class="red-band__text">www.keelbracketworks.com.au</p>
</section>

<section class="card card--back" aria-label="Card back">
  <div class="product-photo" role="img" aria-label="Photo of the bracket kit installed with wiring"></div>
  <p class="tagline">Made In Australia</p>
  <div class="tread-band"></div>
  <div class="brand"><span class="brand__mark"></span><span class="brand__name">Steadfast Bracket Kit</span></div>
  <div class="contact">
    <p class="contact__name">Dana Whitford</p>
    <p class="contact__role">President</p>
    <ul class="contact__list">
      <li class="contact__item">
        <svg class="contact__icon" viewBox="0 0 18 18"><circle cx="9" cy="9" r="8" fill="none" stroke="#c8202f" stroke-width="1.5"/><rect x="6" y="4" width="6" height="10" rx="1" fill="none" stroke="#c8202f" stroke-width="1.4"/></svg>
        0400 218 604
      </li>
      <li class="contact__item">
        <svg class="contact__icon" viewBox="0 0 18 18"><circle cx="9" cy="9" r="8.5" fill="#c8202f"/><rect x="4.5" y="6" width="9" height="6.5" fill="none" stroke="#fff" stroke-width="1.2"/><path d="M4.5 6 L9 9.5 L13.5 6" fill="none" stroke="#fff" stroke-width="1.2"/></svg>
        sales@keelbracketworks.com.au
      </li>
    </ul>
  </div>
  <div class="red-band"></div>
  <p class="red-band__text">Call Us! 1300 555 014</p>
</section>

</body>
</html>
```